Business card design needed

I need a business card that sets my business apart from big gyms and intimidating personal trainers. My personal training business focuses on outdoor and client in-home training, in an environment that is both enjoyable and sustainable for the client.
I train males and females, however a large proportion of my clientelle are female, so I would like the card to lean towards females, but still have a bit of masculine appeal about it.
My business colours are a deep sky blue and lightish red/orange (as seen in logo)

Contact Information for Business Card

Stride & Vigour Mentor
Feel stronger, live brighter, every day!
Benedict Rowlan- Health and Fitness Professional
Locations all across the Yarra Valley and Eastern Suburbs of Melbourne
0438152906
benedictrowlanpt@mailora.com.au

Requirements
Must have
• - Mobile number must stand out
- The 'Locations all across the Yarra Valley and Eastern Suburbs of Melbourne' must be clear and easy to read (different colour maybe?)

```html
<!DOCTYPE html>
<html lang="en">
<head>
<meta charset="UTF-8">
<title>Benedict Rowlan Health and Fitness – Business Card</title>
<link rel="stylesheet" href="https://fonts.googleapis.com/css2?family=Arimo:wght@400;700&family=Nunito:wght@700;800&family=Tenor+Sans&display=swap">
<style>
  :root {
    --sky-blue: #2f8fe8;
    --brand-red: #f03a10;
    --ink: #111111;
    --paper: #ffffff;
  }
  html, body {
    margin: 0;
    padding: 0;
    overflow: hidden;
    background: var(--paper);
  }
  .card {
    position: relative;
    width: 1200px;
    height: 694px;
    background: var(--paper);
    overflow: hidden;
  }
  .card__stripes {
    position: absolute;
    inset: 0;
    width: 1200px;
    height: 694px;
  }
  .brand {
    position: absolute;
    top: 140px;
    left: 0;
    width: 1200px;
    display: flex;
    flex-direction: column;
    align-items: center;
  }
  .brand__name {
    font-family: "Nunito", sans-serif;
    font-weight: 800;
    font-size: 46px;
    line-height: 1.1;
    color: var(--sky-blue);
  }
  .brand__tagline {
    font-family: "Nunito", sans-serif;
    font-weight: 800;
    font-size: 26px;
    line-height: 1.3;
    color: var(--brand-red);
  }
  .contact {
    position: absolute;
    left: 0;
    width: 1200px;
    margin: 0;
    text-align: center;
    white-space: nowrap;
  }
  .contact__business {
    top: 278px;
    font-family: "Tenor Sans", sans-serif;
    font-variant: small-caps;
    font-size: 50px;
    line-height: 60px;
    color: var(--ink);
    letter-spacing: 0.5px;
  }
  .contact__phone {
    top: 334px;
    font-family: "Arimo", sans-serif;
    font-size: 62px;
    line-height: 72px;
    color: var(--brand-red);
  }
  .contact__locations {
    top: 405px;
    font-family: "Nunito", sans-serif;
    font-weight: 800;
    font-size: 39px;
    line-height: 50px;
    color: var(--sky-blue);
  }
  .contact__email {
    top: 528px;
    font-family: "Arimo", sans-serif;
    font-size: 31px;
    line-height: 40px;
    color: var(--ink);
  }
</style>
</head>
<body>
  <main class="card">
    <svg class="card__stripes" viewBox="0 0 1200 694" aria-hidden="true">
      <rect x="0" y="0" width="1200" height="70" fill="var(--brand-red)"/>
      <rect x="0" y="80" width="1200" height="12" fill="var(--sky-blue)"/>
      <rect x="0" y="602" width="1200" height="12" fill="var(--sky-blue)"/>
      <rect x="0" y="624" width="1200" height="70" fill="var(--brand-red)"/>
    </svg>

    <header class="brand">
      <span class="brand__name">Stride &amp; Vigour Mentor</span>
      <span class="brand__tagline">Feel stronger, live brighter, every day!</span>
    </header>

    <p class="contact contact__business">Benedict Rowlan Health and Fitness</p>
    <p class="contact contact__phone">Phone: 0438152906</p>
    <p class="contact contact__locations">Professional Locations all across the<br>Yarra Valley and Eastern Suburbs of Melbourne</p>
    <p class="contact contact__email">benedictrowlanpt@mailora.com.au</p>
  </main>
</body>
</html>
```